KTR Engineering Business Card Design

We’re looking for an elegant, clean, and timeless business card design that communicates experience, capability, and reliability.

KTR Engineering was established in 1995 , we are a Government Contracting company providing Professional Services to the Ministry of Harbor Works, Frontier Stewardship and the Waypoint Consortium. Our capabilities include: Acquisition & Program Management; Intelligence & Security Operations; Cyber, IT & Network Operations; Lifecycle Logistics & Asset Readiness; C5ISR Systems Engineering & Sustainment.

We want the card to reflect a straightforward, confident approach to business. The design should feel polished and professional without being flashy or overly corporate.

Design Direction
Clean, sophisticated, and uncluttered
Elegant but understated
Strong typography and thoughtful spacing
A timeless aesthetic rather than something overly trendy
Confident and established, with a sense of substance
Easy to read and practical in a real-world business setting

The overall impression should be: “These are experienced professionals who know what they’re doing, do what they say, and can be relied upon.”

We’re open to creative interpretations. The finished card should feel distinctive through its typography, proportions, layout, and attention to detail rather than through excessive graphics or visual effects.

We’re looking for a design that would make a potential client immediately feel that they’re dealing with a capable, trustworthy, and established company.

Company Colors: Navy and Gold/Yellow (but you do not need to use these colors on the card)
Company Name: KTR Engineering Associates, Inc. (known as KTR Engineering)
Website: ktrengineering.example
Company Logo: Navy & Gold (other variations attached)

```html
<!DOCTYPE html>
<html lang="en">
<head>
<meta charset="utf-8">
<title>KTR Engineering Business Card</title>
<link href="https://fonts.googleapis.com/css2?family=Arimo:wght@400;700&display=swap" rel="stylesheet">
<style>
  :root {
    --backdrop: #1b1b1b;
    --card-light: #f2f2f2;
    --navy: #1f2a5e;
    --ink: #222326;
    --rule: #2a2f45;
  }
  html, body {
    margin: 0;
    padding: 0;
    overflow: hidden;
  }
  body {
    width: 1200px;
    height: 1059px;
    background: var(--backdrop);
    position: relative;
    font-family: "Arimo", Arial, sans-serif;
  }
  .card {
    position: absolute;
    border-radius: 18px;
    box-shadow: 0 10px 24px rgba(0,0,0,0.55);
  }
  .card--front {
    left: 257px;
    top: 89px;
    width: 687px;
    height: 390px;
    background: var(--card-light);
  }
  .card--back {
    left: 254px;
    top: 547px;
    width: 693px;
    height: 393px;
    background: var(--navy);
  }
  .wordmark {
    position: absolute;
    margin: 0;
    font-weight: 700;
    line-height: 1;
    letter-spacing: 1px;
  }
  .card--front .wordmark {
    right: 76px;
    top: 80px;
    font-size: 81px;
    color: var(--navy);
  }
  .card--back .wordmark {
    left: 0;
    right: 0;
    top: 155px;
    text-align: center;
    font-size: 118px;
    color: var(--card-light);
  }
  .person {
    position: absolute;
    left: 38px;
    top: 192px;
  }
  .person__name {
    margin: 0;
    font-size: 25px;
    font-weight: 700;
    color: var(--navy);
    line-height: 1.1;
  }
  .person__title {
    margin: 1px 0 0;
    font-size: 18.5px;
    color: var(--ink);
    line-height: 1.2;
  }
  .divider {
    position: absolute;
    left: 38px;
    right: 38px;
    top: 254px;
    height: 0;
    border-top: 1px solid var(--rule);
  }
  .contacts {
    position: absolute;
    left: 37px;
    top: 267px;
    margin: 0;
    padding: 0;
    list-style: none;
  }
  .contacts__item {
    display: flex;
    align-items: center;
    height: 31px;
    font-size: 18.5px;
    color: var(--ink);
  }
  .contacts__icon {
    width: 13px;
    height: 13px;
    margin-right: 9px;
    fill: var(--navy);
    flex: none;
  }
</style>
</head>
<body>
  <section class="card card--front" aria-label="Business card front">
    <p class="wordmark">KTR</p>
    <div class="person">
      <h1 class="person__name">Maren T. Holloway</h1>
      <p class="person__title">Principal Engineer</p>
    </div>
    <div class="divider"></div>
    <ul class="contacts">
      <li class="contacts__item">
        <svg class="contacts__icon" viewBox="0 0 24 24" aria-hidden="true"><path d="M6.6 10.8c1.4 2.8 3.8 5.1 6.6 6.6l2.2-2.2c.3-.3.7-.4 1-.2 1.1.4 2.3.6 3.6.6.6 0 1 .4 1 1V20c0 .6-.4 1-1 1C10.6 21 3 13.4 3 4c0-.6.4-1 1-1h3.5c.6 0 1 .4 1 1 0 1.3.2 2.5.6 3.6.1.3 0 .7-.2 1L6.6 10.8z"/></svg>
        (555) 278-9041
      </li>
      <li class="contacts__item">
        <svg class="contacts__icon" viewBox="0 0 24 24" aria-hidden="true"><path d="M2 9l10-7 10 7v12H2V9zm2 1.2V19h16v-8.8l-8 5.6-8-5.6z"/></svg>
        m.h@ktrengineering.example
      </li>
      <li class="contacts__item">
        <svg class="contacts__icon" viewBox="0 0 24 24" aria-hidden="true"><path d="M12 2a10 10 0 1 0 0 20 10 10 0 0 0 0-20zm-1 17.9A8 8 0 0 1 4.1 10L9 15v1c0 1.1.9 2 2 2v1.9zm6.9-2.5c-.3-.8-1-1.4-1.9-1.4h-1v-3c0-.6-.4-1-1-1H8v-2h2c.6 0 1-.4 1-1V7h2c1.1 0 2-.9 2-2v-.4a8 8 0 0 1 2.9 12.8z"/></svg>
        ktrengineering.example
      </li>
    </ul>
  </section>

  <section class="card card--back" aria-label="Business card back">
    <p class="wordmark">KTR</p>
  </section>
</body>
</html>
```